Webpage Needed for Bright Harbor Wiring Electrical and Security

We need a web design for our company showing people we arent just a small business. We want to look big so people can trust us. I would like information from my business cards on the page. example, we do all house rennovations, construction, commercial, 24 hour emergency service, new installations, repairs, maintenance, home theatre and so on...

I would also like images from my facebook on the page and linked. facebook.com/brightharborwiring

Target Market(s)

builders, residents,

Industry/Entity Type

Business

Number of Pages Required

1 page

Font styles to use
Other font styles liked:
• Juice bold

Requirements
Must have
• colours the same as the logo. background must be white. also the font must be Juice Bold which is the font of the logo
Should not have
• black as the background

```html
<!DOCTYPE html>
<html lang="en">
<head>
<meta charset="utf-8">
<title>Bright Harbor Wiring Electrical and Security</title>
<link rel="stylesheet" href="https://fonts.googleapis.com/css2?family=Electrolize&family=Lato:wght@400;700&display=swap">
<style>
  :root {
    --blue: #4cbbea;
    --orange: #f58c5a;
    --ink: #1c1c1c;
    --rule: #e6e6e6;
    --white: #ffffff;
    --hero-dark: #1e1f21;
    --hero-mid: #55585c;
    --hero-light: #cfd3d6;
    --shop-light: #d9dcdd;
    --shop-mid: #7d8386;
    --shop-green: #3f8a5a;
  }
  * { box-sizing: border-box; margin: 0; padding: 0; }
  html, body { width: 673px; height: 1200px; overflow: hidden; background: var(--white); }
  body { position: relative; font-family: "Electrolize", "Lato", sans-serif; color: var(--ink); }
  a { color: inherit; text-decoration: none; }

  .brand { position: absolute; left: 48px; top: 30px; width: 140px; display: flex; align-items: center; gap: 7px; }
  .brand-mark { width: 12px; height: 12px; border-radius: 50%; background: var(--blue); flex: none; }
  .brand-name { font-size: 15px; line-height: 17px; color: var(--ink); }

  .main-nav { position: absolute; right: 45px; top: 47px; display: flex; align-items: center; gap: 27px; font-size: 14px; letter-spacing: 0.5px; }
  .nav-link.is-active { border-bottom: 1px solid var(--ink); padding-bottom: 2px; }
  .nav-button { background: var(--orange); color: var(--white); border-radius: 5px; padding: 2px 12px; font-size: 13px; }

  .rule { position: absolute; left: 48px; width: 580px; height: 1px; background: var(--rule); }

  .hero { position: absolute; left: 42px; top: 116px; width: 598px; height: 303px; }
  .hero-photo { position: absolute; inset: 0;
    background: linear-gradient(100deg, var(--hero-light) 0%, #e9ecee 30%, var(--hero-mid) 52%, var(--hero-dark) 70%, #3a3b3c 100%); }
  .hero-title { position: absolute; right: 10px; top: 36px; font-size: 39px; font-weight: 400; color: var(--white); letter-spacing: 1px; }
  .hero-text { position: absolute; left: 398px; top: 90px; width: 162px; font-size: 12.5px; line-height: 14px; color: var(--white); letter-spacing: 0.8px; }
  .hero-button { position: absolute; left: 477px; top: 168px; width: 91px; height: 26px; background: var(--blue); color: var(--white); border-radius: 4px; font-size: 16px; text-align: center; line-height: 26px; letter-spacing: 0.5px; }

  .section-title { position: absolute; left: 0; width: 673px; text-align: center; font-size: 40px; font-weight: 400; letter-spacing: 2px; }
  .section-title.services { top: 460px; color: var(--blue); }
  .section-title.contact { top: 864px; color: var(--orange); }

  .services-photo { position: absolute; left: 42px; top: 541px; width: 357px; height: 273px;
    background: linear-gradient(180deg, #3c4347 0%, var(--shop-mid) 30%, var(--shop-light) 55%, #a7abab 75%, var(--shop-green) 88%, #8f9394 100%); }
  .services-copy { position: absolute; left: 411px; top: 538px; width: 205px; }
  .services-heading { font-size: 16px; line-height: 19px; text-transform: uppercase; letter-spacing: 1px; font-weight: 400; margin-bottom: 2px; }
  .services-heading .tone-blue { color: var(--blue); }
  .services-heading .tone-orange { color: var(--orange); }
  .services-text { width: 192px; font-family: "Lato", sans-serif; font-size: 13.5px; line-height: 17.6px; }

  .contact-block { position: absolute; left: 0; width: 673px; text-align: center; }
  .contact-label { font-size: 20px; letter-spacing: 1px; font-weight: 400; }
  .contact-value { font-size: 14px; letter-spacing: 1px; margin-top: 2px; }
  .tone-blue { color: var(--blue); }
  .tone-orange { color: var(--orange); }

  .social-list { position: absolute; left: 280px; top: 1113px; display: flex; gap: 14px; list-style: none; }
  .social-item { width: 31px; height: 31px; border-radius: 3px; display: block; }
  .social-item.one { background: var(--blue); }
  .social-item.two { background: var(--orange); }
  .social-item.three { background: var(--ink); }

  .footer-note { position: absolute; left: 0; width: 673px; top: 1172px; text-align: center; font-size: 10px; letter-spacing: 0.5px; }
</style>
</head>
<body>
  <header>
    <a class="brand" href="#home"><span class="brand-mark"></span><span class="brand-name">Bright Harbor Wiring</span></a>
    <nav class="main-nav">
      <a class="nav-link is-active" href="#home">Home</a>
      <a class="nav-link" href="#services">Services</a>
      <a class="nav-button" href="#contact">Contact</a>
    </nav>
  </header>
  <div class="rule" style="top:93px"></div>

  <section class="hero" id="home">
    <div class="hero-photo" role="img" aria-label="Company work ute with ladder on the roof rack parked inside a workshop"></div>
    <h1 class="hero-title">Need some help?</h1>
    <p class="hero-text">We can help you with house rennovations, construction, 24 hours emergencies, and others services.</p>
    <a class="hero-button" href="#services">Services</a>
  </section>

  <h2 class="section-title services" id="services">Services</h2>
  <div class="rule" style="top:513px"></div>
  <div class="services-photo" role="img" aria-label="Workshop interior with stored pipes, benches and green trolleys"></div>
  <div class="services-copy">
    <h3 class="services-heading">Bright <span class="tone-blue">Harbor</span> <span class="tone-orange">Wiring</span> Electrical and Security</h3>
    <p class="services-text">We cover 24 hour emergency service and all new electrical installations, repairs, maintenance, renovations/extensions, re-wiring, home theatre, surround sound, wall tv's, electric hot water, stoves, cooktops, lighting, ceiling fans, testing and tagging, data, telephone and security systems.</p>
  </div>

  <h2 class="section-title contact" id="contact">Contact</h2>
  <div class="rule" style="top:921px"></div>
  <div class="contact-block" style="top:946px">
    <h4 class="contact-label">Email us</h4>
    <p class="contact-value"><span class="tone-orange">alex@</span>bright<span class="tone-blue">harbor</span><span class="tone-orange">wiring</span>.com</p>
  </div>
  <div class="contact-block" style="top:1011px">
    <h4 class="contact-label">Call us</h4>
    <p class="contact-value">0400 <span class="tone-blue">555</span> <span class="tone-orange">218</span></p>
  </div>
  <div class="contact-block" style="top:1075px">
    <h4 class="contact-label">Connect with us</h4>
  </div>
  <ul class="social-list">
    <li><a class="social-item one" href="#" aria-label="Social profile one"></a></li>
    <li><a class="social-item two" href="#" aria-label="Social profile two"></a></li>
    <li><a class="social-item three" href="#" aria-label="Social profile three"></a></li>
  </ul>
  <div class="rule" style="top:1155px"></div>
  <footer class="footer-note">Bright Harbor Wiring Copyright© 2015</footer>
</body>
</html>
```